Rosquillas de Maíz y Queso

Necesitamos el de una bolsa que sea parcialmente transparente, para este producto, nuestra empresa se llama TOVALSA (Comercial Tovalsa), estamos ubicados en Honduras. Este un producto típico de Honduras, Este producto es para consumo masivo y será vendido en supermercados.
Adjunto ejemplos de empaques de este producto ya existentes.
Updates

Es nuestra primera vez, y queremos revisar bien los diseños, adicionalmente unos nos llegaron ayer y queremos unos pequeños cambios para poder decidir. Gracias

Target Market(s)

Clientes en supermercados

Industry/Entity Type

Panaderia

Requirements
Must have
• La bolsa debe ser transparente con ventana para ver el producto
Nice to have
• Tiene que tener una ventana grande la bolsa o ser la mayor parte transparente para mostrar el producto

```html
<!DOCTYPE html>
<html lang="es">
<head>
<meta charset="UTF-8">
<title>Rosquillas de queso – Tovalsa</title>
<link href="https://fonts.googleapis.com/css2?family=Fredoka:wght@500;700&family=Lobster&family=Roboto:wght@500&display=swap" rel="stylesheet">
<style>
  :root{
    --stage:#ededf0;
    --purple-deep:#2b1670;
    --purple:#4a2596;
    --yellow:#f6c81c;
    --blue:#3a9be8;
    --blue-dark:#1d5fb0;
    --white:#ffffff;
    --green:#2e8b3a;
  }
  *{margin:0;padding:0;box-sizing:border-box}
  html,body{width:1200px;height:998px;overflow:hidden;background:var(--stage)}
  .canvas{position:relative;width:1200px;height:998px}
  .bag{position:absolute;left:320px;top:89px;width:560px;height:820px}
  .bag-art{position:absolute;inset:0}
  .brand{position:absolute;left:36px;top:108px;font-family:"Fredoka",sans-serif;font-weight:700;
    font-size:30px;line-height:1;color:var(--purple-deep);letter-spacing:2px}
  .title{position:absolute;left:34px;top:255px;font-family:"Fredoka",sans-serif;font-weight:700;
    font-size:92px;line-height:1;color:var(--blue);
    -webkit-text-stroke:3px var(--white);paint-order:stroke fill;
    text-shadow:0 5px 0 var(--blue-dark),0 8px 12px rgba(0,0,0,.35)}
  .subtitle{position:absolute;left:46px;top:360px;font-family:"Fredoka",sans-serif;font-weight:700;
    font-size:38px;line-height:1;color:var(--blue);-webkit-text-stroke:1.5px var(--white);paint-order:stroke fill}
  .claim{position:absolute;left:92px;top:548px;font-family:"Lobster",sans-serif;color:var(--white);
    line-height:.95;text-shadow:0 2px 4px rgba(0,0,0,.4)}
  .claim-percent{display:block;font-size:30px;padding-left:10px}
  .claim-word{display:block;font-size:38px}
  .net-weight{position:absolute;left:66px;top:692px;width:92px;height:62px;border:2px solid var(--white);
    font-family:"Roboto",sans-serif;font-weight:500;color:var(--white);font-size:15px;
    text-align:center;line-height:1.3;padding-top:8px}
</style>
</head>
<body>
<div class="canvas">
  <div class="bag">
    <svg class="bag-art" width="560" height="820" viewBox="0 0 560 820">
      <defs>
        <linearGradient id="bodyGrad" x1="0" y1="0" x2="1" y2="1">
          <stop offset="0" stop-color="#5a2aa8"/>
          <stop offset=".5" stop-color="#3a1c86"/>
          <stop offset="1" stop-color="#2b1670"/>
        </linearGradient>
        <linearGradient id="glowGrad" x1="0" y1="0" x2="1" y2="0">
          <stop offset="0" stop-color="#c02fa0" stop-opacity="0"/>
          <stop offset=".6" stop-color="#b02ca8" stop-opacity=".5"/>
          <stop offset="1" stop-color="#7b3bb8" stop-opacity=".2"/>
        </linearGradient>
        <radialGradient id="windowGrad" cx=".5" cy=".5" r=".6">
          <stop offset="0" stop-color="#f3d3a2"/>
          <stop offset=".6" stop-color="#d9a062"/>
          <stop offset="1" stop-color="#b87a3e"/>
        </radialGradient>
        <radialGradient id="cheeseGrad" cx=".5" cy=".45" r=".6">
          <stop offset="0" stop-color="#ffe27a" stop-opacity=".95"/>
          <stop offset=".7" stop-color="#f2b416" stop-opacity=".7"/>
          <stop offset="1" stop-color="#f2b416" stop-opacity="0"/>
        </radialGradient>
        <radialGradient id="cornGrad" cx=".5" cy=".45" r=".6">
          <stop offset="0" stop-color="#f5c542" stop-opacity=".95"/>
          <stop offset=".65" stop-color="#c9a32a" stop-opacity=".7"/>
          <stop offset="1" stop-color="#6f9a3a" stop-opacity="0"/>
        </radialGradient>
      </defs>

      <rect x="0" y="0" width="560" height="820" fill="url(#bodyGrad)"/>
      <path d="M150 820 C 260 560, 330 360, 560 200 L560 820 Z" fill="url(#glowGrad)"/>

      <path d="M0 0 L420 0 C 360 70, 280 130, 190 190 C 120 235, 55 262, 0 272 Z" fill="var(--yellow)"/>
      <path d="M420 0 L452 0 C 390 78, 300 140, 205 200 C 135 246, 60 274, 0 284 L0 272 C 55 262,120 235,190 190 C 280 130,360 70,420 0 Z" fill="var(--white)" opacity=".9"/>

      <path d="M320 300 C 420 270, 540 280, 548 340 L548 640 C 540 710, 440 720, 380 690 C 350 670, 345 620, 345 560 C 345 480, 300 420, 300 360 C 300 330, 305 305, 320 300 Z"
        fill="url(#windowGrad)" role="img" aria-label="Ventana transparente que muestra las rosquillas de maíz y queso"/>

      <ellipse cx="190" cy="472" rx="100" ry="58"
        fill="url(#cheeseGrad)" role="img" aria-label="Ilustración de un trozo de queso con salpicadura de queso derretido"/>

      <ellipse cx="285" cy="672" rx="52" ry="86"
        fill="url(#cornGrad)" role="img" aria-label="Ilustración de una mazorca de maíz con granos sueltos"/>

      <circle cx="445" cy="690" r="38" fill="var(--white)" stroke="var(--green)" stroke-width="5"/>

      <g fill="var(--purple-deep)">
        <rect x="0" y="0" width="560" height="52" opacity=".25"/>
        <rect x="0" y="768" width="560" height="52"/>
      </g>
      <g stroke="#ffffff" stroke-opacity=".22" stroke-width="2">
        <line x1="0" y1="10" x2="560" y2="10"/><line x1="0" y1="20" x2="560" y2="20"/>
        <line x1="0" y1="30" x2="560" y2="30"/><line x1="0" y1="40" x2="560" y2="40"/>
        <line x1="0" y1="778" x2="560" y2="778"/><line x1="0" y1="788" x2="560" y2="788"/>
        <line x1="0" y1="798" x2="560" y2="798"/><line x1="0" y1="808" x2="560" y2="808"/>
      </g>
    </svg>

    <div class="brand">TOVALSA</div>
    <div class="title">Rosquillas</div>
    <div class="subtitle">de queso</div>
    <div class="claim"><span class="claim-percent">100%</span><span class="claim-word">Organic</span></div>
    <div class="net-weight">NET WT.<br>240g</div>
  </div>
</div>
</body>
</html>
```